Intranet for company management ERP Style

We need a redesign for our Intranet webpage (Images, CSS), we have all the code and functionality ready and a basic design but it is not good looking. In order to meet our company standards this design has to be fully responsive and elegant, also should display the colors of the company: (#F17808 #EDAA64 #F4B947 #F2A900 #292828 #3D3D3D #062953) usually Dark orange colors are the main ones, though we wouldn't mind to see other options or to implement a pair of skins that we could switch easily on the webpage.
Access to the webpage can be granted

Target Market(s)

this webpage is for internal use of the company but could also be sold to external customers in the future, our market is cryptocurrency and BPO

Industry/Entity Type

BPO, Cryptocurrency

Coding

Coded - Design and coding required

Number of Pages Required

1 page

Font styles to use
Other font styles liked:
• Headings: Montserrat Extra Bold, Sub headings: Montserrat, Text: Object Sans

Colors
F0912C
F2A743
F7CA91
FBE8D2
FDF5EE

Requirements
Nice to have
• elegant icons designs and menus

```html
<!DOCTYPE html>
<html lang="en">
<head>
<meta charset="utf-8">
<title>Intranet Dashboard – Light and Dark Skins</title>
<link href="https://fonts.googleapis.com/css2?family=Nunito:wght@300;400;600;700;800&family=Nunito+Sans:wght@400;600;700&display=swap" rel="stylesheet">
<style>
  :root{
    --stage-dark:#2e2e2e;
    --stage-orange:#f0912c;
    --orange:#f0912c;
    --orange-strong:#f17808;
    --blue:#2f9ee0;
    --purple:#b14ad6;
    --yellow:#f4c21f;
    --green:#4dba5a;
    --grey-rank:#8d8d8d;
    --cream:#fdf5ee;
  }
  *{box-sizing:border-box;margin:0;padding:0}
  html,body{width:859px;height:1200px;overflow:hidden}
  body{position:relative;background:var(--stage-dark);font-family:"Nunito Sans",sans-serif}
  .stage-wave{position:absolute;left:0;top:0;width:859px;height:1200px}
  .mode-title{position:absolute;left:109px;font-family:"Nunito",sans-serif;font-weight:300;font-size:38px;color:#fff;letter-spacing:.2px}
  .mode-title--light{top:58px}
  .mode-title--dark{top:655px}

  /* ---------- card shell ---------- */
  .shell{position:absolute;width:610px;height:343px;border-radius:14px;overflow:hidden}
  .shell--back{left:109px}
  .shell--front{left:140px}
  .light .shell--back{top:178px;background:#222}
  .light .shell--front{top:152px;background:linear-gradient(100deg,#f09032 0%,#e48050 45%,#d5737a 75%,#c06aa0 100%)}
  .dark .shell--back{top:775px;background:linear-gradient(100deg,#f09032 0%,#e48050 45%,#d5737a 75%,#c06aa0 100%)}
  .dark .shell--front{top:749px;background:#222222}

  /* sidebar */
  .avatar{position:absolute;border-radius:8px;background:linear-gradient(150deg,#6f7e4a,#2f3a26 55%,#8a6a55)}
  .side-avatar{left:17px;top:16px;width:31px;height:31px}
  .user-name{position:absolute;left:17px;top:55px;font-family:"Nunito",sans-serif;font-weight:700;font-size:8px;color:#fff}
  .user-mail{position:absolute;left:17px;top:66px;font-size:5.6px;color:rgba(255,255,255,.75)}
  .nav{position:absolute;left:17px;top:93px;list-style:none}
  .nav li{height:22px;display:flex;align-items:center;font-size:6px;font-weight:600;color:rgba(255,255,255,.75)}
  .nav li.is-active{color:#fff;font-weight:700}
  .nav svg{width:10px;height:10px;margin-right:9px;fill:none;stroke:currentColor;stroke-width:1.3;stroke-linecap:round;stroke-linejoin:round}
  .dark .shell--front .nav li{color:#b9b9b9}
  .dark .shell--front .nav li.is-active{color:#fff}
  .powered{position:absolute;left:17px;top:296px;font-size:5.6px;color:rgba(255,255,255,.6)}
  .brand{position:absolute;left:17px;top:309px;display:flex;align-items:center;gap:4px;font-family:"Nunito Sans",sans-serif;font-weight:700;font-size:8px;color:#fff}
  .brand i{width:7px;height:7px;border-radius:50%;background:#fff;display:block}
  .dark .shell--front .brand i,.light .shell--back .brand i{background:var(--orange)}

  /* main panel */
  .panel{position:absolute;left:112px;top:8.5px;width:489px;height:326px;border-radius:14px;overflow:hidden}
  .light .panel{background:#fff}
  .dark .shell--front .panel{background:#2c2c2c}
  .light .shell--back .panel{background:#2c2c2c}
  .dark .shell--back .panel{background:#fff}
  .aside{position:absolute;left:347px;top:0;width:142px;height:100%}
  .light .aside{background:var(--cream)}
  .dark .shell--front .aside{background:#313131}
  .light .shell--back .aside{background:#313131}
  .dark .shell--back .aside{background:var(--cream)}

  .page-title{position:absolute;left:24px;top:17px;font-family:"Nunito",sans-serif;font-weight:800;font-size:16px;letter-spacing:.2px}
  .page-date{position:absolute;left:24px;top:38px;font-size:6px}
  .search{position:absolute;left:180px;top:22px;width:92px;height:17px;border-radius:9px;display:flex;align-items:center;justify-content:space-between;padding:0 7px;font-size:6px}
  .round-btn{position:absolute;top:22px;width:17px;height:17px;border-radius:50%;display:flex;align-items:center;justify-content:center}
  .round-btn--chat{left:280px}
  .round-btn--bell{left:305px}
  .round-btn--chat::after{content:"";position:absolute;right:1px;top:0;width:3.5px;height:3.5px;border-radius:50%;background:var(--orange-strong)}
  .search svg,.round-btn svg{width:7px;height:7px;fill:none;stroke:currentColor;stroke-width:1.3;stroke-linecap:round}

  .light .page-title{color:#2d2d2d}
  .light .page-date,.light .search{color:#8d8d8d}
  .light .search,.light .round-btn{background:#f4f4f4;color:#8d8d8d}
  .dark .page-title{color:#fff}
  .dark .page-date{color:#a5a5a5}
  .dark .search,.dark .round-btn{background:#383838;color:#a5a5a5}

  .stat{position:absolute;top:60px;width:91px;height:51px;border-radius:7px}
  .stat--csat{left:24px}.stat--qa{left:128px}.stat--psat{left:231px}
  .stat-label{position:absolute;left:9px;top:10px;font-size:6.3px;font-weight:600}
  .stat-value{position:absolute;right:10px;top:21px;font-family:"Nunito",sans-serif;font-weight:800;font-size:11px}
  .stat-sub{position:absolute;right:10px;top:36px;font-size:5.8px}
  .stat svg{position:absolute;left:9px;top:32px;width:27px;height:12px}
  .stat--csat .stat-value{color:var(--orange)}
  .stat--qa .stat-value{color:var(--blue)}
  .stat--psat .stat-value{color:var(--purple)}
  .light .stat--csat{background:#fdf1e6}
  .light .stat--qa{background:#e9f4fc}
  .light .stat--psat{background:#f7e9f9}
  .light .stat-label{color:#2d2d2d}
  .light .stat-sub{color:#8d8d8d}
  .dark .stat--csat{background:#3b322b}
  .dark .stat--qa{background:#2d3640}
  .dark .stat--psat{background:#382f3c}
  .dark .stat-label{color:#fff}
  .dark .stat-sub{color:#a5a5a5}

  .agenda-head{position:absolute;left:24px;width:299px;font-family:"Nunito",sans-serif;font-weight:600;font-size:8px;padding-bottom:5px;border-bottom:1px solid}
  .agenda-head--today{top:135px}
  .agenda-head--tomorrow{top:232px}
  .event{position:absolute;left:24px;display:flex;align-items:flex-start}
  .event-icon{width:19px;height:19px;border-radius:50%;display:flex;align-items:center;justify-content:center;margin-right:8px;margin-top:0}
  .event-icon svg{width:7px;height:7px;fill:none;stroke:currentColor;stroke-width:1.2;stroke-linecap:round;stroke-linejoin:round}
  .event-title{font-size:6.2px;font-weight:700;line-height:1;margin-top:1px}
  .event-time{font-size:5.8px;margin-top:5px}
  .event--orange .event-icon{color:var(--orange)}
  .event--blue .event-icon{color:var(--blue)}
  .event--purple .event-icon{color:var(--purple)}
  .event--green .event-icon{color:var(--green)}
  .light .event--orange .event-icon{background:#fdf0e3}
  .light .event--blue .event-icon{background:#e7f3fc}
  .light .event--purple .event-icon{background:#f6e8f9}
  .light .event--green .event-icon{background:#e9f6ea}
  .dark .event--orange .event-icon{background:#3e3530}
  .dark .event--blue .event-icon{background:#303a43}
  .dark .event--purple .event-icon{background:#3b3240}
  .dark .event--green .event-icon{background:#303c31}
  .light .agenda-head,.light .event-title{color:#2d2d2d}
  .light .agenda-head{border-color:#ececec}
  .light .event-time{color:#8d8d8d}
  .dark .agenda-head,.dark .event-title{color:#fff}
  .dark .agenda-head{border-color:#3c3c3c}
  .dark .event-time{color:#a5a5a5}

  .aside-title{position:absolute;left:17px;top:17px;font-family:"Nunito",sans-serif;font-weight:600;font-size:8px}
  .aside-link{position:absolute;right:18px;top:19px;font-size:6px}
  .people{position:absolute;left:17px;top:39px;width:107px;list-style:none}
  .person{position:relative;height:36px;display:flex;align-items:center;border-bottom:1px solid}
  .person:last-child{border-bottom:none}
  .rank{width:8.5px;height:8.5px;border-radius:50%;font-size:5px;font-weight:700;color:#fff;display:flex;align-items:center;justify-content:center;margin-right:9px}
  .rank--1{background:var(--yellow)}.rank--2{background:var(--blue)}.rank--3{background:var(--purple)}.rank--4,.rank--5{background:var(--grey-rank)}
  .person-photo{width:18px;height:18px;border-radius:50%;margin-right:8px}
  .person-name{font-size:6.2px;font-weight:700;line-height:1}
  .person-score{font-size:6px;margin-top:3px}
  .light .aside-title,.light .person-name{color:#2d2d2d}
  .light .aside-link,.light .person-score{color:#8d8d8d}
  .light .person{border-color:#efe4da}
  .dark .aside-title,.dark .person-name{color:#fff}
  .dark .aside-link,.dark .person-score{color:#a5a5a5}
  .dark .person{border-color:#5a5a5a}

  .news{position:absolute;left:18px;top:223px;width:106px;height:89px;border-radius:7px}
  .news-title{position:absolute;left:12px;top:11px;font-family:"Nunito",sans-serif;font-weight:600;font-size:8px}
  .news-photo{position:absolute;left:12px;top:28px;width:25px;height:25px;border-radius:4px;background:linear-gradient(135deg,#dfe4ea,#f5f3f4 50%,#c9d3df)}
  .news-text{position:absolute;left:43px;top:28px;width:56px;font-size:6px;line-height:8.5px}
  .news-button{position:absolute;left:12px;top:61px;width:83px;height:20px;border-radius:5px;display:flex;align-items:center;justify-content:center;font-size:6px;font-weight:700;color:var(--orange)}
  .light .news{background:#fff;box-shadow:0 2px 8px rgba(220,170,130,.18)}
  .light .news-title{color:#2d2d2d}
  .light .news-text{color:#6d6d6d}
  .light .news-button{background:#fdf0e3}
  .dark .news{background:#484646}
  .dark .news-title{color:#fff}
  .dark .news-text{color:#c9c9c9}
  .dark .news-button{background:#5a4a3e}

  .spark-csat{stroke:var(--orange)}.spark-qa{stroke:var(--blue)}.spark-psat{stroke:var(--purple)}
</style>
</head>
<body>

<svg class="stage-wave" viewBox="0 0 859 1200" aria-hidden="true">
  <path fill="#f0912c" d="M0 629 C80 592 165 566 235 568 C300 572 295 650 350 648 C500 640 700 574 859 563 L859 1200 L0 1200 Z"/>
</svg>

<h1 class="mode-title mode-title--light">Light Mode</h1>
<h1 class="mode-title mode-title--dark">Dark Mode</h1>

<!-- ================= LIGHT SKIN ================= -->
<section class="light">
  <div class="shell shell--back">
    <div class="avatar side-avatar" role="img" aria-label="Profile photo of Marisol"></div>
    <p class="user-name">Marisol</p>
    <p class="user-mail">m.reyes@northline.io</p>
    <ul class="nav">
      <li class="is-active"><svg viewBox="0 0 12 12"><path d="M2 9a4 4 0 1 1 8 0z"/><path d="M6 8.5 8 5.5"/></svg></li>
      <li><svg viewBox="0 0 12 12"><path d="M3 1h4.5L9.5 3v8H3z"/></svg></li>
      <li><svg viewBox="0 0 12 12"><path d="M2 11h9M3 10V8M5 10V6M7 10V4M9 10V2"/></svg></li>
      <li><svg viewBox="0 0 12 12"><circle cx="6" cy="6" r="5"/></svg></li>
      <li><svg viewBox="0 0 12 12"><rect x="2" y="2.5" width="8" height="8.5" rx="1"/></svg></li>
      <li><svg viewBox="0 0 12 12"><rect x="1.5" y="2" width="9" height="2.5"/><path d="M2.5 4.5V11h7V4.5"/></svg></li>
      <li><svg viewBox="0 0 12 12"><rect x="1.5" y="1.5" width="9" height="4"/><rect x="1.5" y="6.5" width="9" height="4"/></svg></li>
    </ul>
    <p class="powered">Powered by</p>
    <p class="brand"><i></i>Northline</p>
    <div class="panel"><div class="aside"></div></div>
  </div>

  <div class="shell shell--front">
    <div class="avatar side-avatar" role="img" aria-label="Profile photo of Marisol"></div>
    <p class="user-name">Marisol</p>
    <p class="user-mail">m.reyes@northline.io</p>
    <ul class="nav">
      <li class="is-active"><svg viewBox="0 0 12 12"><path d="M2 9a4 4 0 1 1 8 0z"/><path d="M6 8.5 8 5.5"/></svg>Dashboard</li>
      <li><svg viewBox="0 0 12 12"><path d="M3 1h4.5L9.5 3v8H3z"/><path d="M4.5 5.5h3M4.5 7.5h3"/></svg>Requests</li>
      <li><svg viewBox="0 0 12 12"><path d="M2 11h9M3 10V8M5 10V6M7 10V4M9 10V2"/></svg>Reports</li>
      <li><svg viewBox="0 0 12 12"><circle cx="6" cy="6" r="5"/><path d="M4.7 4.6a1.4 1.4 0 1 1 1.8 1.3c-.4.2-.5.5-.5 1M6 8.7v.1"/></svg>Helpdesk</li>
      <li><svg viewBox="0 0 12 12"><rect x="2" y="2.5" width="8" height="8.5" rx="1"/><path d="M4 1.5v2M8 1.5v2M4 6h4M4 8h2"/></svg>Payroll</li>
      <li><svg viewBox="0 0 12 12"><rect x="1.5" y="2" width="9" height="2.5"/><path d="M2.5 4.5V11h7V4.5M4.5 6.5h3"/></svg>Suggestion Box</li>
      <li><svg viewBox="0 0 12 12"><rect x="1.5" y="1.5" width="9" height="4"/><rect x="1.5" y="6.5" width="9" height="4"/><path d="M3.5 3.5h1M3.5 8.5h1"/></svg>Administrator</li>
    </ul>
    <p class="powered">Powered by</p>
    <p class="brand"><i></i>Northline</p>

    <div class="panel">
      <h2 class="page-title">Dashboard</h2>
      <p class="page-date">01 - 31 January 2022</p>
      <div class="search">Search<svg viewBox="0 0 10 10"><circle cx="4" cy="4" r="3"/><path d="M6.3 6.3 9 9"/></svg></div>
      <div class="round-btn round-btn--chat"><svg viewBox="0 0 10 10"><path d="M5 1a4 3.6 0 1 1-2 6.8L1 9l.6-2.2A4 3.6 0 0 1 5 1z"/></svg></div>
      <div class="round-btn round-btn--bell"><svg viewBox="0 0 10 10"><path d="M2 7.5h6L7.3 6V4a2.3 2.3 0 0 0-4.6 0v2zM4 9h2"/></svg></div>

      <div class="stat stat--csat"><span class="stat-label">CSAT</span><span class="stat-value">3.5</span><span class="stat-sub">72, 243,83</span>
        <svg viewBox="0 0 27 12"><path d="M0 11 7 6 13 9 20 4 27 2V12H0z" fill="#f0912c" opacity=".15"/><polyline class="spark-csat" points="0,11 7,6 13,9 20,4 27,2" fill="none" stroke-width=".8"/></svg></div>
      <div class="stat stat--qa"><span class="stat-label">QA</span><span class="stat-value">5.0</span><span class="stat-sub">72, 243,83</span>
        <svg viewBox="0 0 27 12"><path d="M0 11 7 6 13 9 20 4 27 2V12H0z" fill="#2f9ee0" opacity=".15"/><polyline class="spark-qa" points="0,11 7,6 13,9 20,4 27,2" fill="none" stroke-width=".8"/></svg></div>
      <div class="stat stat--psat"><span class="stat-label">PSAT</span><span class="stat-value">4.7</span><span class="stat-sub">72, 243,83</span>
        <svg viewBox="0 0 27 12"><path d="M0 11 7 6 13 9 20 4 27 2V12H0z" fill="#b14ad6" opacity=".15"/><polyline class="spark-psat" points="0,11 7,6 13,9 20,4 27,2" fill="none" stroke-width=".8"/></svg></div>

      <h3 class="agenda-head agenda-head--today">Today</h3>
      <div class="event event--orange" style="top:160px"><span class="event-icon"><svg viewBox="0 0 8 8"><rect x="1" y="1.5" width="6" height="5.5" rx=".6"/><path d="M2.7 4.4l1 1 1.8-1.8"/></svg></span><div><p class="event-title">Meeting with the boss</p><p class="event-time">2:30 pm at Beverly hills</p></div></div>
      <div class="event event--blue" style="top:188px"><span class="event-icon"><svg viewBox="0 0 8 8"><rect x="1" y="1.5" width="6" height="5.5" rx=".6"/><path d="M2.7 4.4l1 1 1.8-1.8"/></svg></span><div><p class="event-title">Help Owen on his task for the year</p><p class="event-time">2:30 pm at Beverly hills</p></div></div>

      <h3 class="agenda-head agenda-head--tomorrow">Tomorrow</h3>
      <div class="event event--purple" style="top:257px"><span class="event-icon"><svg viewBox="0 0 8 8"><rect x="1" y="1.5" width="6" height="5.5" rx=".6"/><path d="M2.7 4.4l1 1 1.8-1.8"/></svg></span><div><p class="event-title">Meeting with the boss at the palace</p><p class="event-time">2:30 pm at Beverly hills</p></div></div>
      <div class="event event--green" style="top:285px"><span class="event-icon"><svg viewBox="0 0 8 8"><rect x="1" y="1.5" width="6" height="5.5" rx=".6"/><path d="M2.7 4.4l1 1 1.8-1.8"/></svg></span><div><p class="event-title">Meet with Ada in the garden</p><p class="event-time">2:30 pm at Beverly hills</p></div></div>

      <aside class="aside">
        <h3 class="aside-title">Top People</h3>
        <span class="aside-link">View All</span>
        <ol class="people">
          <li class="person"><span class="rank rank--1">1</span><span class="person-photo" role="img" aria-label="Photo of Nora Vance" style="background:linear-gradient(135deg,#c9c2bb,#3c2e2a)"></span><div><p class="person-name">Nora Vance</p><p class="person-score">2134</p></div></li>
          <li class="person"><span class="rank rank--2">2</span><span class="person-photo" role="img" aria-label="Photo of Ada Brooks" style="background:linear-gradient(135deg,#5a2a4a,#1e1420)"></span><div><p class="person-name">Ada Brooks</p><p class="person-score">1923</p></div></li>
          <li class="person"><span class="rank rank--3">3</span><span class="person-photo" role="img" aria-label="Photo of Marisol Reyes" style="background:linear-gradient(135deg,#6f7e4a,#2f3a26)"></span><div><p class="person-name">Marisol Reyes</p><p class="person-score">1829</p></div></li>
          <li class="person"><span class="rank rank--4">4</span><span class="person-photo" role="img" aria-label="Photo of Owen Parker" style="background:linear-gradient(135deg,#9aa3a8,#4a4a4a)"></span><div><p class="person-name">Owen Parker</p><p class="person-score">392</p></div></li>
          <li class="person"><span class="rank rank--5">5</span><span class="person-photo" role="img" aria-label="Photo of Lena Ortiz" style="background:linear-gradient(135deg,#f2d24b,#9a7a22)"></span><div><p class="person-name">Lena Ortiz</p><p class="person-score">232</p></div></li>
        </ol>
        <div class="news">
          <h4 class="news-title">What's new!</h4>
          <div class="news-photo" role="img" aria-label="Holiday greeting card photo"></div>
          <p class="news-text">Happy holidays everyone! Enjoy your food...</p>
          <span class="news-button">Read more</span>
        </div>
      </aside>
    </div>
  </div>
</section>

<!-- ================= DARK SKIN ================= -->
<section class="dark">
  <div class="shell shell--back">
    <div class="avatar side-avatar" role="img" aria-label="Profile photo of Marisol"></div>
    <p class="user-name">Marisol</p>
    <p class="user-mail">m.reyes@northline.io</p>
    <ul class="nav">
      <li class="is-active"><svg viewBox="0 0 12 12"><path d="M2 9a4 4 0 1 1 8 0z"/><path d="M6 8.5 8 5.5"/></svg></li>
      <li><svg viewBox="0 0 12 12"><path d="M3 1h4.5L9.5 3v8H3z"/></svg></li>
      <li><svg viewBox="0 0 12 12"><path d="M2 11h9M3 10V8M5 10V6M7 10V4M9 10V2"/></svg></li>
      <li><svg viewBox="0 0 12 12"><circle cx="6" cy="6" r="5"/></svg></li>
      <li><svg viewBox="0 0 12 12"><rect x="2" y="2.5" width="8" height="8.5" rx="1"/></svg></li>
      <li><svg viewBox="0 0 12 12"><rect x="1.5" y="2" width="9" height="2.5"/><path d="M2.5 4.5V11h7V4.5"/></svg></li>
      <li><svg viewBox="0 0 12 12"><rect x="1.5" y="1.5" width="9" height="4"/><rect x="1.5" y="6.5" width="9" height="4"/></svg></li>
    </ul>
    <p class="powered">Powered by</p>
    <p class="brand"><i></i>Northline</p>
    <div class="panel"><div class="aside"></div></div>
  </div>

  <div class="shell shell--front">
    <div class="avatar side-avatar" role="img" aria-label="Profile photo of Marisol"></div>
    <p class="user-name">Marisol</p>
    <p class="user-mail">m.reyes@northline.io</p>
    <ul class="nav">
      <li class="is-active"><svg viewBox="0 0 12 12"><path d="M2 9a4 4 0 1 1 8 0z"/><path d="M6 8.5 8 5.5"/></svg>Dashboard</li>
      <li><svg viewBox="0 0 12 12"><path d="M3 1h4.5L9.5 3v8H3z"/><path d="M4.5 5.5h3M4.5 7.5h3"/></svg>Requests</li>
      <li><svg viewBox="0 0 12 12"><path d="M2 11h9M3 10V8M5 10V6M7 10V4M9 10V2"/></svg>Reports</li>
      <li><svg viewBox="0 0 12 12"><circle cx="6" cy="6" r="5"/><path d="M4.7 4.6a1.4 1.4 0 1 1 1.8 1.3c-.4.2-.5.5-.5 1M6 8.7v.1"/></svg>Helpdesk</li>
      <li><svg viewBox="0 0 12 12"><rect x="2" y="2.5" width="8" height="8.5" rx="1"/><path d="M4 1.5v2M8 1.5v2M4 6h4M4 8h2"/></svg>Payroll</li>
      <li><svg viewBox="0 0 12 12"><rect x="1.5" y="2" width="9" height="2.5"/><path d="M2.5 4.5V11h7V4.5M4.5 6.5h3"/></svg>Suggestion Box</li>
      <li><svg viewBox="0 0 12 12"><rect x="1.5" y="1.5" width="9" height="4"/><rect x="1.5" y="6.5" width="9" height="4"/><path d="M3.5 3.5h1M3.5 8.5h1"/></svg>Administrator</li>
    </ul>
    <p class="powered">Powered by</p>
    <p class="brand"><i></i>Northline</p>

    <div class="panel">
      <h2 class="page-title">Dashboard</h2>
      <p class="page-date">01 - 31 January 2022</p>
      <div class="search">Search<svg viewBox="0 0 10 10"><circle cx="4" cy="4" r="3"/><path d="M6.3 6.3 9 9"/></svg></div>
      <div class="round-btn round-btn--chat"><svg viewBox="0 0 10 10"><path d="M5 1a4 3.6 0 1 1-2 6.8L1 9l.6-2.2A4 3.6 0 0 1 5 1z"/></svg></div>
      <div class="round-btn round-btn--bell"><svg viewBox="0 0 10 10"><path d="M2 7.5h6L7.3 6V4a2.3 2.3 0 0 0-4.6 0v2zM4 9h2"/></svg></div>

      <div class="stat stat--csat"><span class="stat-label">CSAT</span><span class="stat-value">3.5</span><span class="stat-sub">72, 243,83</span>
        <svg viewBox="0 0 27 12"><path d="M0 11 7 6 13 9 20 4 27 2V12H0z" fill="#f0912c" opacity=".15"/><polyline class="spark-csat" points="0,11 7,6 13,9 20,4 27,2" fill="none" stroke-width=".8"/></svg></div>
      <div class="stat stat--qa"><span class="stat-label">QA</span><span class="stat-value">5.0</span><span class="stat-sub">72, 243,83</span>
        <svg viewBox="0 0 27 12"><path d="M0 11 7 6 13 9 20 4 27 2V12H0z" fill="#2f9ee0" opacity=".15"/><polyline class="spark-qa" points="0,11 7,6 13,9 20,4 27,2" fill="none" stroke-width=".8"/></svg></div>
      <div class="stat stat--psat"><span class="stat-label">PSAT</span><span class="stat-value">4.7</span><span class="stat-sub">72, 243,83</span>
        <svg viewBox="0 0 27 12"><path d="M0 11 7 6 13 9 20 4 27 2V12H0z" fill="#b14ad6" opacity=".15"/><polyline class="spark-psat" points="0,11 7,6 13,9 20,4 27,2" fill="none" stroke-width=".8"/></svg></div>

      <h3 class="agenda-head agenda-head--today">Today</h3>
      <div class="event event--orange" style="top:160px"><span class="event-icon"><svg viewBox="0 0 8 8"><rect x="1" y="1.5" width="6" height="5.5" rx=".6"/><path d="M2.7 4.4l1 1 1.8-1.8"/></svg></span><div><p class="event-title">Meeting with the boss</p><p class="event-time">2:30 pm at Beverly hills</p></div></div>
      <div class="event event--blue" style="top:188px"><span class="event-icon"><svg viewBox="0 0 8 8"><rect x="1" y="1.5" width="6" height="5.5" rx=".6"/><path d="M2.7 4.4l1 1 1.8-1.8"/></svg></span><div><p class="event-title">Help Owen on his task for the year</p><p class="event-time">2:30 pm at Beverly hills</p></div></div>

      <h3 class="agenda-head agenda-head--tomorrow">Tomorrow</h3>
      <div class="event event--purple" style="top:257px"><span class="event-icon"><svg viewBox="0 0 8 8"><rect x="1" y="1.5" width="6" height="5.5" rx=".6"/><path d="M2.7 4.4l1 1 1.8-1.8"/></svg></span><div><p class="event-title">Meeting with the boss at the palace</p><p class="event-time">2:30 pm at Beverly hills</p></div></div>
      <div class="event event--green" style="top:285px"><span class="event-icon"><svg viewBox="0 0 8 8"><rect x="1" y="1.5" width="6" height="5.5" rx=".6"/><path d="M2.7 4.4l1 1 1.8-1.8"/></svg></span><div><p class="event-title">Meet with Ada in the garden</p><p class="event-time">2:30 pm at Beverly hills</p></div></div>

      <aside class="aside">
        <h3 class="aside-title">Top People</h3>
        <span class="aside-link">View All</span>
        <ol class="people">
          <li class="person"><span class="rank rank--1">1</span><span class="person-photo" role="img" aria-label="Photo of Nora Vance" style="background:linear-gradient(135deg,#c9c2bb,#3c2e2a)"></span><div><p class="person-name">Nora Vance</p><p class="person-score">2134</p></div></li>
          <li class="person"><span class="rank rank--2">2</span><span class="person-photo" role="img" aria-label="Photo of Ada Brooks" style="background:linear-gradient(135deg,#5a2a4a,#1e1420)"></span><div><p class="person-name">Ada Brooks</p><p class="person-score">1923</p></div></li>
          <li class="person"><span class="rank rank--3">3</span><span class="person-photo" role="img" aria-label="Photo of Marisol Reyes" style="background:linear-gradient(135deg,#6f7e4a,#2f3a26)"></span><div><p class="person-name">Marisol Reyes</p><p class="person-score">1829</p></div></li>
          <li class="person"><span class="rank rank--4">4</span><span class="person-photo" role="img" aria-label="Photo of Owen Parker" style="background:linear-gradient(135deg,#9aa3a8,#4a4a4a)"></span><div><p class="person-name">Owen Parker</p><p class="person-score">392</p></div></li>
          <li class="person"><span class="rank rank--5">5</span><span class="person-photo" role="img" aria-label="Photo of Lena Ortiz" style="background:linear-gradient(135deg,#f2d24b,#9a7a22)"></span><div><p class="person-name">Lena Ortiz</p><p class="person-score">232</p></div></li>
        </ol>
        <div class="news">
          <h4 class="news-title">What's new!</h4>
          <div class="news-photo" role="img" aria-label="Holiday greeting card photo"></div>
          <p class="news-text">Happy holidays everyone! Enjoy your food...</p>
          <span class="news-button">Read more</span>
        </div>
      </aside>
    </div>
  </div>
</section>

</body>
</html>
```